Verano Suisse: Symposium annuel 2018

You created the flyer "Atelier Dorvanne" for us at the beginning of the year. We would like to work in a new version. More details can be found in the briefing! Flyer (red, gray, black) - flyer wants to be white! - Flyer wants to be White! All further information can be found in the document in the appendix!

```html
<!DOCTYPE html>
<html lang="fr">
<head>
<meta charset="utf-8">
<title>Verano Suisse – Atelier Dorvanne</title>
<link href="https://fonts.googleapis.com/css2?family=Montserrat:wght@300;500;600;700;800&display=swap" rel="stylesheet">
<style>
  :root {
    --page-bg: #d9d9d9;
    --paper: #ffffff;
    --paper-tint: #eef0f2;
    --ink: #111111;
    --ink-soft: #3a3a3a;
    --red: #e0141e;
    --red-deep: #b0080f;
    --pill-dark: #120607;
    --pill-red: #4a0a0c;
    --violet: #6a2ca0;
    --navy: #0f1f45;
    --blue: #1c3f94;
  }
  * { margin: 0; padding: 0; box-sizing: border-box; }
  html, body { width: 1200px; height: 1200px; overflow: hidden; }
  body {
    background: var(--page-bg);
    font-family: "Montserrat", Arial, sans-serif;
    color: var(--ink);
    position: relative;
  }
  .flyer {
    position: absolute;
    left: 0; top: 176px;
    width: 1200px; height: 848px;
    background: radial-gradient(ellipse at 35% 30%, var(--paper-tint) 0%, var(--paper) 60%);
    overflow: hidden;
  }
  .brand {
    position: absolute; left: 41px; top: 44px;
    display: flex; align-items: center; gap: 10px;
  }
  .brand-square { width: 30px; height: 70px; background: var(--ink); }
  .brand-name {
    font-weight: 800; font-size: 34px; line-height: 35px;
    letter-spacing: 2px; color: var(--ink); text-transform: uppercase;
  }
  .hero-visual {
    position: absolute; left: 88px; top: 20px;
    width: 560px; height: 740px;
    background: radial-gradient(ellipse at 55% 50%, rgba(106,44,160,0.22) 0%, rgba(106,44,160,0.08) 40%, rgba(230,232,236,0.35) 70%, rgba(255,255,255,0) 100%);
  }
  .content { position: absolute; left: 646px; top: 0; width: 500px; }
  .title-light {
    position: absolute; top: 44px; left: 0;
    font-weight: 300; font-size: 92px; letter-spacing: -1px;
    color: var(--ink-soft); white-space: nowrap;
  }
  .title-bold {
    position: absolute; top: 134px; left: 2px;
    font-weight: 800; font-size: 84px; letter-spacing: -2px;
    color: var(--red); white-space: nowrap;
    background: linear-gradient(180deg, #f0242c 0%, var(--red-deep) 100%);
    -webkit-background-clip: text; background-clip: text;
    -webkit-text-fill-color: transparent;
  }
  .date-pill {
    position: absolute; top: 253px; left: 3px;
    width: 444px; height: 72px; border-radius: 36px;
    background: linear-gradient(90deg, var(--pill-dark) 0%, var(--pill-red) 100%);
    display: flex; align-items: center; justify-content: center;
    font-weight: 700; font-size: 56px; letter-spacing: -2px; color: #fff;
  }
  .date-pill .day { color: var(--red); margin-right: 12px; }
  .audience-title {
    position: absolute; top: 350px; left: 4px;
    font-weight: 800; font-size: 52px; letter-spacing: -1px; color: var(--red);
  }
  .audience {
    position: absolute; top: 409px; left: 6px;
    font-weight: 600; font-size: 20px; letter-spacing: -0.3px;
  }
  .intro {
    position: absolute; top: 440px; left: 6px; width: 500px;
    font-weight: 600; font-size: 17.5px; line-height: 25px; letter-spacing: -0.3px;
  }
  .topics {
    position: absolute; top: 512px; left: 4px; width: 480px;
    list-style: none; display: flex; flex-wrap: wrap; column-gap: 10px;
    font-weight: 300; font-size: 18.5px; line-height: 31px; color: var(--ink-soft);
  }
  .topics li { display: flex; align-items: center; }
  .topics li::before {
    content: ""; width: 13px; height: 13px; border-radius: 50%;
    background: var(--red); margin-right: 6px;
  }
  .topics .break { flex-basis: 100%; height: 0; }
  .contact {
    position: absolute; top: 615px; left: -7px;
    width: 491px; height: 87px;
    border: 1.5px solid var(--red); padding: 14px 12px;
  }
  .contact-label { font-weight: 600; font-size: 20px; letter-spacing: -0.4px; white-space: nowrap; }
  .contact-email { font-weight: 600; font-size: 23px; color: var(--red); margin-top: 4px; }
  .partners {
    position: absolute; top: 737px; left: -7px; width: 491px; height: 33px;
    display: flex; align-items: center; justify-content: space-between;
    font-family: "Montserrat", Arial, sans-serif; white-space: nowrap;
  }
  .partner { font-weight: 600; font-size: 15px; }
  .partner-calvoria { color: var(--violet); font-size: 18px; }
  .partner-nerima { color: var(--blue); }
  .partner-ostrand { color: var(--red); font-size: 12px; }
  .partner-tavello { color: var(--blue); font-size: 19px; letter-spacing: 1px; }
  .partner-lumira {
    background: var(--navy); color: #fff; font-size: 10px;
    padding: 11px 7px; letter-spacing: 0.5px;
  }
</style>
</head>
<body>
  <main class="flyer">
    <div class="hero-visual" role="img" aria-label="Illustration du système lymphatique humain en violet sur fond de molécules gris clair"></div>

    <div class="brand">
      <span class="brand-square"></span>
      <span class="brand-name">Verano<br>Suisse</span>
    </div>

    <section class="content">
      <h1>
        <span class="title-light">ATELIER</span>
        <span class="title-bold">DORVANNE</span>
      </h1>
      <div class="date-pill"><span class="day">21</span>AVRIL 2019</div>

      <h2 class="audience-title">DESTINATEUR</h2>
      <p class="audience">PHYSIOTHERAPES, LYMPHOTHERAPEUTE</p>
      <p class="intro">Programmeapres une introduction sur les actualites dans la prise en charge des pathologies lymphatique nous organisons des ateliers pratique</p>

      <ul class="topics">
        <li>Drainage</li>
        <li>Bandage</li>
        <li>Compression elastique</li>
        <span class="break"></span>
        <li>les outils etc</li>
      </ul>

      <div class="contact">
        <p class="contact-label">INSCRIPTION ET RENSEIGNEMENT VIA EMAIL</p>
        <p class="contact-email">info@veranosuisse.ch</p>
      </div>

      <div class="partners">
        <span class="partner partner-calvoria">calvoria</span>
        <span class="partner partner-nerima">Nerima Med</span>
        <span class="partner partner-ostrand">Ostrand &amp; Pell</span>
        <span class="partner partner-tavello">TAVELLO</span>
        <span class="partner partner-lumira">LUMIRA</span>
      </div>
    </section>
  </main>
</body>
</html>
```